Business Card template designs

We need a lot of Business card designs.
Your designs will get exposure on our newly opened business-card printing website.
We are committed to quality of paper and packages we use, so they will come up very fancy.

Here is your advantage. We will put the profile of the graphic designer on our site so that you can showcase your designs to people around the world and in Japan.

A profile is not mandatory, although we encourage graphic designers to have a profile to get continuous work in the future.
We are looking forward to having many good designs.

The right of the use of design will be owned by us.
The design may be used to the products other than
business cards.

Target Market(s)

designer,photographer,creator,artist

Industry/Entity Type

Printing

Contact Information for Business Card

The back design is important.
Please check the reference file.

Requirements
Must have
• Please include the following, required information on your business card designs.
• Name: Haruka Tanabe
• Title: Designer
• Web: https://www.korimo.co.jp/kr/
• Address: 4-17 Kitaharazono-Cho Nerima-ku, Tokyo
• Email: info@kkorimo.com
• Phone: 03 6184 3970
• Mobile: 070 4213 6087
• * For Japanese sites, we will convert the text portion to Japanese characters.
• * In case of 28mmx70mm only include Name,Enail,Phone and SNS account(https://www.facebook.com/kkorimo.com)
• 1. colorful
• 2. simple
• 3. natural
• 4. modern
• 5. cool
• 6. sporty
• Please make variations of the same image with 3-6
• different colors / patterns for one design so that
• customers can compare and choose.
• If you want to use a same picture, please make make
• copies and paste on each different types of design.
Nice to have
• You may also use, the following non-required information.
• Company Name: Korimo, Inc.
• Fax: 03-6471-2093
• Open space for company logo

```html
<!DOCTYPE html>
<html lang="en">
<head>
<meta charset="utf-8">
<title>Haruka Tanabe – Business Card</title>
<link rel="stylesheet" href="https://fonts.googleapis.com/css2?family=Montserrat:wght@500;600&family=Open+Sans:wght@400&display=swap">
<style>
  :root {
    --page-bg: #ffffff;
    --brand-blue: #1a93d2;
    --brand-blue-deep: #0b76bd;
    --band-light: #8dcfe9;
    --name-front: #a9def6;
    --name-back: #ffffff;
    --text-grey: #555555;
    --rule-blue: #3aa6e0;
    --card-edge: #2b2b2b;
  }
  * { margin: 0; padding: 0; box-sizing: border-box; }
  html, body {
    width: 1200px;
    height: 1095px;
    overflow: hidden;
    background: var(--page-bg);
  }
  .card {
    position: absolute;
    left: 279px;
    width: 620px;
    height: 345px;
    border: 1.5px solid var(--card-edge);
    box-shadow: 7px 8px 9px rgba(0, 0, 0, 0.35);
    overflow: hidden;
    background: #fff;
  }
  .card--front { top: 151px; background: var(--brand-blue); }
  .card--back { top: 595px; }

  .pattern-field {
    position: absolute;
    background: linear-gradient(200deg, var(--brand-blue-deep) 0%, rgba(11,118,189,0.55) 45%, rgba(26,147,210,0) 100%);
  }
  .card--front .pattern-field { left: 110px; top: 0; width: 510px; height: 345px; }
  .card--back .pattern-field { left: 390px; top: 0; width: 230px; height: 174px; }

  .name {
    position: absolute;
    left: 0;
    width: 100%;
    text-align: center;
    font-family: "Montserrat", sans-serif;
    font-weight: 500;
    text-transform: uppercase;
    line-height: 1;
  }
  .title {
    position: absolute;
    left: 0;
    width: 100%;
    text-align: center;
    font-family: "Open Sans", sans-serif;
    font-weight: 400;
    text-transform: uppercase;
    line-height: 1;
  }
  .card--front .name { top: 141px; font-size: 33px; letter-spacing: 6px; color: var(--name-front); }
  .card--front .title { top: 191px; font-size: 21px; letter-spacing: 3px; color: var(--name-front); }

  .back-header {
    position: absolute;
    left: 0; top: 0;
    width: 100%;
    height: 174px;
    background: var(--brand-blue);
  }
  .card--back .name { top: 96px; font-size: 26px; letter-spacing: 5px; color: var(--name-back); font-weight: 600; }
  .card--back .title { top: 134px; font-size: 18px; letter-spacing: 2.5px; color: var(--name-back); }
  .accent-band {
    position: absolute;
    left: 0; top: 174px;
    width: 100%;
    height: 22px;
    background: var(--band-light);
  }

  .contact {
    position: absolute;
    left: 0;
    width: 100%;
    text-align: center;
    font-family: "Open Sans", sans-serif;
    font-size: 15.5px;
    color: var(--text-grey);
    line-height: 1;
  }
  .contact--phone { top: 208px; }
  .contact--mobile { top: 227px; }
  .contact--address { top: 260px; font-size: 16.5px; }
  .contact--email { top: 288px; font-size: 16.5px; }
  .contact--web { top: 309px; font-size: 16.5px; }
  .rule {
    position: absolute;
    left: 138px;
    width: 339px;
    height: 1.5px;
    background: var(--rule-blue);
  }
  .rule--top { top: 253px; }
  .rule--bottom { top: 281px; }
</style>
</head>
<body>
  <section class="card card--front" aria-label="Card front">
    <div class="pattern-field" role="img" aria-label="Overlapping translucent blue square pattern"></div>
    <h1 class="name">Haruka Tanabe</h1>
    <p class="title">Designer</p>
  </section>

  <section class="card card--back" aria-label="Card back">
    <div class="back-header"></div>
    <div class="pattern-field" role="img" aria-label="Overlapping translucent blue square pattern"></div>
    <h2 class="name">Haruka Tanabe</h2>
    <p class="title">Designer</p>
    <div class="accent-band"></div>
    <p class="contact contact--phone">P: 03 6184 3970</p>
    <p class="contact contact--mobile">M: 070 4213 6087</p>
    <div class="rule rule--top"></div>
    <p class="contact contact--address">4-17 Kitaharazono-Cho Nerima-ku, Tokyo</p>
    <div class="rule rule--bottom"></div>
    <p class="contact contact--email">E: info@kkorimo.com</p>
    <p class="contact contact--web">www.korimo.co.jp/kr/</p>
  </section>
</body>
</html>
```